Kelvo Tech Oz Business card revamp

We are looking to revamp our business card design. We are hoping to change our colours to dark navey blue, gray, white and black but are open to keeping the same if a good design is submited. We are after somthing a bit differnt not just boring business card. I have attached a copy of our current card. We Want to keep the same logo design which i have attached a few to hopfully help you in this process. We are after a design that can be personalized to separate 4 people

Colors
0455a3
ffffff
000000
cbcbcb

Requirements
Must have
• Kelvo Tech Logo, address 3/41 Mallory Court, Wexhill 4218, phone number, Name and position

```html
<!DOCTYPE html>
<html lang="en">
<head>
<meta charset="utf-8">
<title>Kelvo Tech Business Cards</title>
<link rel="stylesheet" href="https://fonts.googleapis.com/css2?family=Arimo:wght@400;700&display=swap">
<style>
  :root {
    --stage: #2b2b2b;
    --card: #ffffff;
    --card-shade: #f0f0f0;
    --brand-blue: #0f5bb5;
    --accent-orange: #ee7623;
    --ink-soft: #7a7a7a;
  }
  * { box-sizing: border-box; margin: 0; padding: 0; }
  html, body {
    width: 1200px; height: 997px; overflow: hidden;
    background: var(--stage);
    font-family: "Arimo", Arial, sans-serif;
  }
  .stage { position: relative; width: 1200px; height: 997px; }
  .card {
    position: absolute; width: 500px; height: 290px;
    background: linear-gradient(160deg, var(--card) 40%, var(--card-shade));
    border-radius: 18px; overflow: hidden;
  }
  .card svg.band { position: absolute; inset: 0; }
  .card--front { left: 70px; top: 300px; }
  .card--back { left: 630px; top: 380px; }

  .brand {
    display: flex; align-items: center; gap: 12px;
    color: var(--brand-blue); font-weight: 700;
  }
  .brand__dot { width: 34px; height: 34px; border-radius: 50%; background: var(--accent-orange); }
  .card--front .brand { position: absolute; left: 110px; top: 95px; font-size: 40px; }
  .card--back .brand { position: absolute; left: 40px; top: 34px; font-size: 30px; }
  .card--back .brand__dot { width: 26px; height: 26px; }

  .showroom {
    position: absolute; right: 30px; top: 196px; text-align: right;
    color: var(--accent-orange); font-size: 13px;
  }
  .address {
    position: absolute; right: 22px; bottom: 12px;
    color: #fff; font-size: 14px;
  }

  .rule { position: absolute; height: 1px; background: var(--accent-orange); }
  .rule--top { left: 300px; right: 18px; top: 96px; }
  .rule--name { left: 150px; right: 250px; top: 150px; }

  .person { position: absolute; left: 40px; top: 124px; }
  .person__name { color: var(--accent-orange); font-weight: 700; font-size: 16px; letter-spacing: .5px; }
  .person__role { color: var(--brand-blue); font-size: 13px; font-weight: 700; margin-top: 2px; }

  .contacts { position: absolute; left: 40px; top: 182px; list-style: none; }
  .contacts li {
    display: flex; align-items: center; gap: 10px;
    color: var(--brand-blue); font-size: 16px; line-height: 24px;
  }
  .contacts svg { width: 16px; height: 16px; flex: none; }

  .website {
    position: absolute; right: 24px; bottom: 40px;
    color: #fff; font-weight: 700; font-size: 15px; letter-spacing: 2px;
  }
</style>
</head>
<body>
<main class="stage">

  <section class="card card--front" aria-label="Business card front">
    <svg class="band" viewBox="0 0 500 290" aria-hidden="true">
      <path d="M0 272 H250 C262 272 266 244 280 244 H500 V290 H0 Z" fill="var(--brand-blue)"/>
      <path d="M0 262 H230 L236 256 H0 Z" fill="var(--accent-orange)"/>
      <path d="M0 256 H236 C230 256 236 262 230 262" fill="none"/>
      <rect x="300" y="232" width="200" height="6" fill="var(--accent-orange)"/>
      <rect x="0" y="256" width="230" height="6" fill="var(--accent-orange)"/>
    </svg>
    <div class="brand"><span class="brand__dot"></span><span class="brand__name">Kelvo Tech</span></div>
    <p class="showroom">Visit our Showroom</p>
    <p class="address">3/41 Mallory Court, Wexhill 4218</p>
  </section>

  <section class="card card--back" aria-label="Business card back">
    <svg class="band" viewBox="0 0 500 290" aria-hidden="true">
      <path d="M0 282 H500 V290 H0 Z" fill="var(--brand-blue)"/>
      <rect x="0" y="272" width="500" height="5" fill="var(--accent-orange)"/>
      <path d="M270 290 V262 C270 242 282 232 300 232 H500 V290 Z" fill="var(--brand-blue)"/>
      <rect x="0" y="262" width="262" height="5" fill="var(--accent-orange)"/>
    </svg>
    <div class="brand"><span class="brand__dot"></span><span class="brand__name">Kelvo Tech</span></div>
    <span class="rule rule--top"></span>
    <div class="person">
      <p class="person__name">DEAN HARLOW</p>
      <p class="person__role">Director</p>
    </div>
    <span class="rule rule--name"></span>
    <ul class="contacts">
      <li>
        <svg viewBox="0 0 16 16" aria-label="Phone"><circle cx="8" cy="8" r="8" fill="var(--accent-orange)"/><path d="M5 4.5h2l.6 2-1 .8a5 5 0 0 0 2.2 2.2l.8-1 2 .6v2c-4 .3-7-2.6-6.6-6.6z" fill="#fff"/></svg>
        (07) 3100 - 2000
      </li>
      <li>
        <svg viewBox="0 0 16 16" aria-label="Mobile"><circle cx="8" cy="8" r="8" fill="var(--accent-orange)"/><rect x="5.5" y="3.5" width="5" height="9" rx="1" fill="#fff"/></svg>
        (07) 3100 - 9000
      </li>
      <li>
        <svg viewBox="0 0 16 16" aria-label="Email"><circle cx="8" cy="8" r="8" fill="var(--accent-orange)"/><rect x="4" y="5" width="8" height="6" fill="#fff"/><path d="M4 5l4 3 4-3" stroke="var(--accent-orange)" fill="none"/></svg>
        info@kelvotech.com
      </li>
    </ul>
    <p class="website">www.kelvotech.com</p>
  </section>

</main>
</body>
</html>
```